Letterhead

We would like to use the logo attached as a new letterhead. Our problem is that we think the dark blue background is too much. We'd like a sleek, professional letterhead, and we'd like at least five options to choose from. I've also uploaded our old letterhead for reference of the style we're going for.

```html
<!DOCTYPE html>
<html lang="en">
<head>
<meta charset="utf-8">
<title>Vellum Ridge Partners – Letterhead</title>
<link rel="stylesheet" href="https://fonts.googleapis.com/css2?family=Figtree:wght@400;500;600&display=swap">
<style>
  :root {
    --backdrop: #e0e0e0;
    --paper: #ffffff;
    --navy: #1b2f4c;
    --navy-heading: #13315a;
    --gold: #c8a766;
    --ink: #2b2b2b;
    --muted: #6b6b6b;
    --footer-text: #ffffff;
  }
  * { margin: 0; padding: 0; box-sizing: border-box; }
  html, body {
    width: 1200px; height: 1200px; overflow: hidden;
    background: var(--backdrop);
    font-family: "Figtree", "Helvetica Neue", Arial, sans-serif;
  }
  .letterhead {
    position: absolute; left: 216px; top: 76px;
    width: 768px; height: 1046px;
    background: var(--paper);
    box-shadow: 0 6px 18px rgba(0,0,0,0.12);
  }
  .brand {
    position: absolute; left: 0; right: 0; top: 62px; height: 80px;
    display: flex; justify-content: center; align-items: center; gap: 14px;
  }
  .brand-mark { width: 24px; height: 24px; background: var(--gold); }
  .brand-name {
    color: var(--navy); font-weight: 600; font-size: 32px;
    letter-spacing: 2px; text-transform: uppercase;
  }
  .greeting {
    position: absolute; left: 52px; top: 242px;
    color: var(--navy-heading); font-weight: 600; font-size: 23px; line-height: 30px;
  }
  .letter-body {
    position: absolute; left: 53px; top: 289px; width: 659px;
    color: var(--ink); font-size: 17.2px; line-height: 26px;
    text-align: justify; letter-spacing: -0.1px;
  }
  .letter-body p + p { margin-top: 26px; }
  .signature-area {
    position: absolute; left: 520px; top: 769px; width: 194px; height: 118px;
    background: radial-gradient(ellipse at center, #ececec 0%, #f7f7f7 60%, #ffffff 100%);
  }
  .sign-off {
    position: absolute; left: 529px; top: 764px;
    color: var(--muted); z-index: 1;
  }
  .sign-name { font-size: 12px; line-height: 16px; }
  .sign-role { font-size: 9.5px; line-height: 16px; }
  .gold-rule {
    position: absolute; left: 0; right: 0; top: 945px; height: 8px;
    background: var(--gold);
  }
  .contact-bar {
    position: absolute; left: 0; right: 0; top: 962px; height: 84px;
    background: var(--navy); color: var(--footer-text);
    font-size: 19.5px;
  }
  .contact-line {
    position: absolute; display: flex; align-items: center; gap: 8px; white-space: nowrap;
  }
  .contact-line svg { flex: none; }
  .phone { left: 161px; top: 14px; }
  .email { left: 161px; top: 39px; }
  .address { left: 386px; top: 16px; line-height: 25px; gap: 12px; }
</style>
</head>
<body>
  <main class="letterhead">
    <header class="brand">
      <span class="brand-mark" aria-hidden="true"></span>
      <span class="brand-name">Vellum Ridge Partners</span>
    </header>

    <h1 class="greeting">Dear Mr. John,</h1>

    <section class="letter-body">
      <p>Lorem ipsum dolor sit amet, consectetuer adipiscing elit, sed diam nonummy nibh euismod tincidunt ut laoreet dolore magna aliquam erat volutpat. Ut wisi enim ad minim veniam, quis nostrud exerci tation ullamcorper suscipit lobortis nisl ut aliquip ex ea commodo consequat. Duis autem vel eum iriure dolor in hendrerit in vulputate velit esse molestie consequat, vel illum dolore eu feugiat nulla facilisis at vero eros et accumsan et iusto odio dignissim qui blandit praesent luptatum zzril delenit augue duis dolore te feugait nulla facilisi.</p>
      <p>Lorem ipsum dolor sit amet, cons ectetuer adipiscing elit, sed diam nonummy nibh euismod tincidunt ut laoreet dolore magna aliquam erat volutpat. Ut wisi Lorem ipsum dolor sit amet, consectetuer adipiscing elit, sed diam nonummy nibh euismod tincidunt ut laoreet dolore magna aliquam erat volutpat. Ut wisi enim ad minim veniam, quis nostrud exerci tation ullamcorper suscipit lobortis nisl ut aliquip ex ea commodo consequat. Duis autem vel eum iriure dolor in hendrerit in vulputate velit esse molestie consequat,Lorem ipsum dolor sit amet, cons ectetuer adipiscing elit, sed diam nonummy nibh euismod tincidunt ut laoreet dolore magna aliquam erat volutpat.</p>
    </section>

    <div class="signature-area" role="img" aria-label="Handwritten signature of the sender"></div>
    <div class="sign-off">
      <div class="sign-name">John Doe</div>
      <div class="sign-role">Office Maneger</div>
    </div>

    <div class="gold-rule"></div>

    <footer class="contact-bar">
      <div class="contact-line phone">
        <svg width="20" height="20" viewBox="0 0 24 24" aria-hidden="true"><path fill="#c8a766" d="M6.6 10.8a15.1 15.1 0 0 0 6.6 6.6l2.2-2.2a1 1 0 0 1 1-.25c1.1.37 2.3.57 3.6.57a1 1 0 0 1 1 1V20a1 1 0 0 1-1 1A17 17 0 0 1 3 4a1 1 0 0 1 1-1h3.5a1 1 0 0 1 1 1c0 1.25.2 2.450.57 3.57a1 1 0 0 1-.25 1z"/></svg>
        <span>555 014 2290</span>
      </div>
      <div class="contact-line email">
        <svg width="20" height="16" viewBox="0 0 24 18" aria-hidden="true"><path fill="#c8a766" d="M0 0h24v18H0z"/><path fill="none" stroke="#1b2f4c" stroke-width="1.8" d="M0 1l12 9 12-9M0 17l8.5-7.5M24 17l-8.5-7.5"/></svg>
        <span>kai@kaidrummel.com</span>
      </div>
      <div class="contact-line address">
        <svg width="20" height="28" viewBox="0 0 20 28" aria-hidden="true"><path fill="#c8a766" d="M10 0a10 10 0 0 0-10 10c0 7 10 18 10 18s10-11 10-18A10 10 0 0 0 10 0zm0 14.5a4.5 4.5 0 1 1 0-9 4.5 4.5 0 0 1 0 9z"/></svg>
        <span>318 Harbor street number 204<br>fairbanks, alaska 99701</span>
      </div>
    </footer>
  </main>
</body>
</html>
```